Tallow Bright business card

Tallow Bright is a new online life insurance company providing instant quotes and policies to consumers.
Target Market(s)
Target market is both business to business as well as business to consumer
Can think out side of the box- We are an open minded bunch
Industry/Entity Type
Life Insurance
Requirements
Must have
- Our corporate Logo
Double sided
Website www.tallowbright.com.au
Phone Number
Name & Position of each person etc.
Modern font

```html
<!DOCTYPE html>
<html lang="en">
<head>
<meta charset="utf-8">
<title>Tallow Bright – Business Card</title>
<link rel="stylesheet" href="https://fonts.googleapis.com/css2?family=Questrial&family=Open+Sans:wght@400;600&display=swap">
<style>
  :root {
    --bg: #ececec;
    --orange-light: #f7a824;
    --orange: #f08c1c;
    --orange-deep: #e46a17;
    --ink: #262626;
    --paper: #ffffff;
    --silver-light: #f4f4f4;
    --silver: #c9c9c9;
    --silver-dark: #a9a9a9;
    --tagline-front: #fbd36a;
    --tagline-back: #e8781a;
  }
  * { box-sizing: border-box; margin: 0; padding: 0; }
  html, body { width: 1200px; height: 951px; overflow: hidden; }
  body {
    background: var(--bg);
    display: flex;
    flex-direction: column;
    align-items: center;
    justify-content: center;
    gap: 44px;
  }
  .card {
    position: relative;
    width: 740px;
    height: 423px;
    overflow: hidden;
    box-shadow: 0 6px 18px rgba(0,0,0,.22);
  }

  /* Brand block */
  .brand {
    font-family: "Questrial", sans-serif;
    color: var(--ink);
    line-height: 1;
  }
  .brand__name { display: block; letter-spacing: -1px; white-space: nowrap; }
  .brand__line {
    display: block;
    white-space: nowrap;
    letter-spacing: 1px;
  }

  /* Front */
  .card--front {
    background: radial-gradient(ellipse at 65% 30%, var(--orange-light) 0%, var(--orange) 45%, var(--orange-deep) 100%);
  }
  .card--front .brand {
    position: absolute;
    left: 64px;
    top: 150px;
  }
  .card--front .brand__name { font-size: 78px; }
  .card--front .brand__line {
    font-size: 26px;
    color: var(--tagline-front);
    margin-top: 14px;
    margin-left: 6px;
  }

  /* Back */
  .card--back {
    background: linear-gradient(135deg, var(--orange-light) 0%, var(--orange) 40%, var(--orange-deep) 100%);
  }
  .back__silver {
    position: absolute;
    top: 0; right: 0; bottom: 0;
    width: 42%;
    background: linear-gradient(90deg, var(--silver-dark) 0%, var(--silver-light) 30%, var(--silver) 100%);
  }
  .card--back .brand {
    position: absolute;
    left: 450px;
    top: 172px;
  }
  .card--back .brand__name { font-size: 38px; }
  .card--back .brand__line {
    font-size: 16px;
    color: var(--tagline-back);
    margin-top: 8px;
    margin-left: 3px;
  }

  .strip {
    position: absolute;
    left: 26px;
    background: var(--paper);
    font-family: "Open Sans", sans-serif;
    color: var(--ink);
    padding: 10px 22px;
    box-shadow: 2px 3px 6px rgba(0,0,0,.25);
    transform: rotate(-4deg);
    transform-origin: left center;
  }
  .strip--name { top: 44px; width: 360px; }
  .strip--phone { top: 150px; width: 370px; }
  .strip--web { top: 262px; width: 360px; }
  .strip__name { font-size: 21px; display: block; }
  .strip__role { font-size: 14px; display: block; margin-left: 4px; }
  .strip__line { font-size: 19px; display: block; line-height: 1.3; white-space: nowrap; }
</style>
</head>
<body>

  <section class="card card--front" aria-label="Business card front">
    <div class="brand">
      <span class="brand__name">Tallow Bright</span>
      <span class="brand__line">COVER. SORTED.</span>
    </div>
  </section>

  <section class="card card--back" aria-label="Business card back">
    <div class="back__silver"></div>

    <div class="strip strip--name">
      <span class="strip__name">Owen Carrick</span>
      <span class="strip__role">Director</span>
    </div>
    <div class="strip strip--phone">
      <span class="strip__line">p: +353 (0)00 555 0142</span>
      <span class="strip__line">m: +353 (0)00 555 0187</span>
    </div>
    <div class="strip strip--web">
      <span class="strip__line">www.tallowbright.com.au</span>
      <span class="strip__line">owen@tallowbright.com.au</span>
    </div>

    <div class="brand">
      <span class="brand__name">Tallow Bright</span>
      <span class="brand__line">COVER. SORTED.</span>
    </div>
  </section>

</body>
</html>
```